Young Accounting firm needing a captivating business card

We need a business card design that forces the person to look at the card because its either gold foil, plastic, or lettering pop up etc. We already have a logo with a specific gold color and we need to make it pop. We are an accounting firm. I need the words" accounting, payroll, licenses, audits, taxes" somewhere on the business card so as to describe what we do- preferably on the side where the logo is at.

Industry/Entity Type

Accounting

Contact Information for Business Card

Address 48276 9th Ave S Ste 305, Federal Way, WA 98117
Business Phone (360)418-2096
Fax (360)418-2157
Office Cell Phone (360)586-7319

Font styles to use
Serif

Colors
85abd2

Requirements
Must have
• It should state
• "Accounting" "Taxes" "Audits" "Licenses" "Payroll"
Nice to have
• Matte with gold foil, different textures, With Either a textured ivory background or gray blue slate background
Should not have
• colorful colors

```html
<!DOCTYPE html>
<html lang="en">
<head>
<meta charset="utf-8">
<title>KLTaxworks Business Card</title>
<link href="https://fonts.googleapis.com/css2?family=Poppins:wght@400;500&display=swap" rel="stylesheet">
<style>
  :root {
    --backdrop: #2a2a2c;
    --card-black: #17171a;
    --pattern-dark: #2b2818;
    --pattern-gold: #3b3520;
    --cream: #e4c878;
    --gold: #d9a93f;
    --copper: #b8743a;
    --slate-blue: #8796b3;
    --ink: #3a3222;
  }
  * { margin: 0; padding: 0; box-sizing: border-box; }
  html, body { width: 1200px; height: 885px; overflow: hidden; }
  body {
    background: var(--backdrop);
    font-family: "Poppins", sans-serif;
    position: relative;
  }
  .card {
    position: absolute;
    left: 259px;
    width: 682px;
    height: 390px;
    border-radius: 4px;
    overflow: hidden;
    box-shadow: 0 10px 30px rgba(0,0,0,.45);
  }
  .card-back { top: 35px; background: var(--card-black); }
  .card-front { top: 460px; background: var(--cream); }

  .back-pattern {
    position: absolute; inset: 0;
    background:
      repeating-linear-gradient(60deg, var(--pattern-dark) 0 14px, var(--card-black) 14px 28px),
      var(--pattern-dark);
    opacity: .9;
  }
  .back-brand {
    position: absolute; right: 36px; top: 120px;
    display: flex; align-items: center; gap: 10px;
    color: var(--gold); font-weight: 500; font-size: 22px;
  }
  .brand-dot {
    width: 16px; height: 16px; border-radius: 50%; background: var(--gold);
  }

  .front-panel { position: absolute; inset: 0; width: 100%; height: 100%; }
  .front-brand {
    position: absolute; right: 56px; top: 150px;
    display: flex; align-items: center; gap: 12px;
    color: var(--gold); font-weight: 500; font-size: 38px; letter-spacing: -.5px;
  }
  .front-brand .brand-dot { width: 22px; height: 22px; }

  .details { position: absolute; left: 40px; top: 58px; color: var(--ink); }
  .person-name { color: var(--copper); font-size: 22px; font-weight: 500; line-height: 1.1; }
  .person-role { color: var(--slate-blue); font-size: 15px; margin-bottom: 14px; }
  .address { font-size: 14px; line-height: 1.35; margin-bottom: 14px; }
  .contact-list { list-style: none; font-size: 14px; line-height: 1.45; }
  .contact-list li { display: flex; align-items: center; gap: 10px; }
  .contact-list svg { width: 13px; height: 13px; fill: var(--copper); flex: none; }
  .services { margin-top: 16px; font-size: 14px; line-height: 1.45; }
  .services .sep { color: var(--copper); margin: 0 5px; }
</style>
</head>
<body>
  <section class="card card-back">
    <div class="back-pattern" role="img" aria-label="Repeating dark gold monogram pattern"></div>
    <div class="back-brand"><span class="brand-dot"></span>KLTaxworks</div>
  </section>

  <section class="card card-front">
    <svg class="front-panel" viewBox="0 0 682 390" preserveAspectRatio="none">
      <polygon points="395,0 682,0 682,300 445,300 318,150" fill="#b8743a"/>
      <polygon points="405,0 682,0 682,290 449,290 327,150" fill="#17171a"/>
    </svg>
    <div class="front-brand"><span class="brand-dot"></span>KLTaxworks</div>

    <div class="details">
      <p class="person-name">Daniel Morrow</p>
      <p class="person-role">Founder &amp; CEO</p>
      <p class="address">48276 9th Ave S Ste 305,<br>Federal Way, WA 98117</p>
      <ul class="contact-list">
        <li><svg viewBox="0 0 16 16"><path d="M3 1l3 3-2 2c1 2 3 4 5 5l2-2 3 3-2 3C6 15 1 10 0 3z"/></svg>(360)418-2096</li>
        <li><svg viewBox="0 0 16 16"><path d="M4 0h8v16H4zM6 2v10h4V2z"/></svg>(360)586-7319</li>
        <li><svg viewBox="0 0 16 16"><path d="M3 0h8v5H3zM0 6h16v8H0zM3 14h10v2H3z"/></svg>(360)418-2157</li>
        <li><svg viewBox="0 0 16 16"><path d="M0 3h16v10H0zM1 4l7 5 7-5z"/></svg>info@kltaxworks.com</li>
        <li><svg viewBox="0 0 16 16"><circle cx="8" cy="8" r="8"/></svg>www.kltaxworks.com</li>
      </ul>
      <p class="services">Accounting<span class="sep">•</span>Taxes<br>Audits<span class="sep">•</span>Licenses<span class="sep">•</span>Payroll</p>
    </div>
  </section>
</body>
</html>
```